Kelvorn LLC web design project

Dallas, TX based water damage mitigation company needs a web site for its new business. The company does water extractions, mitigation, demo, restoration, and reconstruction. We need for the site to have a strong mobile version, and the owners/managers need to be able to edit the site despite having no web design experience. The site needs to look and function, especially the mobile version, similar to marbleforkquiltshop.com if possible.

```html
<!DOCTYPE html>
<html lang="en">
<head>
<meta charset="utf-8">
<title>Kelvorn LLC – Web Design</title>
<link href="https://fonts.googleapis.com/css2?family=Montserrat:wght@400;500;600;700&family=Source+Sans+3:wght@400;600&display=swap" rel="stylesheet">
<style>
:root{
  --navy:#3c4a59;
  --slate:#6e7f92;
  --blue:#0077c0;
  --bg:#eef0f2;
  --white:#ffffff;
  --line:#e3e6ea;
  --text:#7a8592;
}
*{box-sizing:border-box;margin:0;padding:0}
html,body{width:1200px;height:3718px;overflow:hidden}
body{background:var(--bg);font-family:"Source Sans 3",sans-serif;color:var(--navy);position:relative}
.abs{position:absolute}
.mont{font-family:"Montserrat",sans-serif}

/* board header */
.brand-mark{left:300px;top:145px;width:150px;text-align:center}
.brand-name{font-family:"Montserrat",sans-serif;font-weight:700;color:var(--navy);font-size:20px;letter-spacing:1px;white-space:nowrap}
.brand-dot{display:inline-block;width:10px;height:10px;border-radius:50%;background:var(--blue);margin-right:6px;vertical-align:2px}
.vrule{width:1px;height:82px;background:#cfd4da;top:95px}
.board-label{font-family:"Montserrat",sans-serif;font-size:22px;color:var(--navy);font-weight:500}
.font-name{font-size:17px;color:var(--slate)}
.swatch{width:36px;height:36px;border-radius:50%;top:124px}
.hex{font-size:9px;color:var(--slate);top:168px;width:50px;text-align:center}

/* hero */
.hero{position:absolute;left:0;top:0;width:503px;height:281px;overflow:hidden;background:#e6eaee}
.hero-photo{position:absolute;inset:0;background:
  linear-gradient(180deg,rgba(255,255,255,.6) 0%,rgba(255,255,255,0) 35%,rgba(255,255,255,0) 62%,rgba(236,239,242,.9) 78%,#f5f6f8 100%),
  linear-gradient(90deg,#eef2f6 0%,#e1e6ec 18%,#f4f5f7 30%,#d6dbe0 45%,#eceef0 56%,#b9bec4 70%,#8d939a 85%,#6f757c 100%)}
.call-label{left:82px;top:18px;font-size:6px;color:var(--blue);font-family:"Montserrat",sans-serif}
.call-pill{left:66px;top:26px;width:70px;height:16px;border-radius:9px;background:var(--navy);color:#fff;font-size:6px;font-family:"Montserrat",sans-serif;font-weight:600;line-height:16px;padding-left:22px}
.call-icon{position:absolute;left:2px;top:2px;width:12px;height:12px;border-radius:50%;background:#fff}
.call-hours{left:74px;top:46px;font-size:5px;color:var(--blue)}
.hero-logo{left:200px;top:40px;width:103px;text-align:center}
.hero-logo .brand-name{font-size:10px;letter-spacing:.5px}
.hero-menu{left:394px;top:32px;font-size:8px;color:var(--blue);font-family:"Montserrat",sans-serif;font-weight:600}
.banner{left:68px;top:256px;width:368px;height:51px;background:var(--blue);color:#fff;font-family:"Montserrat",sans-serif;font-weight:700;font-size:12px;text-align:center;line-height:51px;letter-spacing:.3px;white-space:nowrap}
.banner--preview{top:232px;height:42px;line-height:42px}

.screen{position:absolute;overflow:hidden;background:#fff}
.screen .scaled{position:absolute;left:0;top:0;width:503px;height:320px;transform-origin:0 0}

/* page */
.page{position:absolute;left:348px;top:828px;width:503px;height:2801px;background:var(--white);overflow:hidden}
.small{font-size:5.4px;line-height:1.9;color:var(--text)}
.rule{height:1px;background:var(--line);left:68px;width:368px}
.sec-title{font-family:"Montserrat",sans-serif;font-weight:600;font-size:11px;color:var(--navy);letter-spacing:.3px;left:0;width:503px;text-align:center}
.tab{height:18px;border:1px solid var(--blue);font-size:4.5px;color:var(--blue);text-align:center;line-height:16px;font-family:"Montserrat",sans-serif;font-weight:600}
.svc-photo{height:67px}
.svc-list{font-size:4.6px;line-height:10.6px;color:var(--text);list-style:none;padding-left:12px}
.svc-list li::before{content:"✓ ";color:var(--navy)}
.btn{background:var(--blue);color:#fff;font-family:"Montserrat",sans-serif;font-weight:600;font-size:4.6px;text-align:center;height:21px;line-height:21px}

.dark{background:var(--navy);left:0;width:503px}
.price-item{width:120px;color:#fff}
.price-item b{font-family:"Montserrat",sans-serif;font-size:5.6px;font-weight:600;display:block}
.price-item span{font-size:4.5px;color:#c8d0d9;line-height:1.7;display:block}
.price-icon{width:14px;height:14px;border:1px solid #dbe1e7;border-radius:3px}
.right{text-align:right}

.bar-wrap{width:115px;height:12px;background:#e8eef5}
.bar{height:12px;color:#fff;font-size:4.2px;line-height:12px;padding:0 5px;display:flex;justify-content:space-between}

.pill-btn{width:55px;height:17px;border-radius:9px;color:#fff;font-size:4.4px;font-family:"Montserrat",sans-serif;font-weight:600;text-align:center;line-height:17px}

.blue-band{background:var(--blue);left:0;width:503px}
.grid-cell{width:123px;height:119px;border:1px solid rgba(255,255,255,.25);padding:30px 14px 0;color:#fff}
.grid-cell b{font-family:"Montserrat",sans-serif;font-size:5.4px;font-weight:600;display:block;margin:8px 0 4px}
.grid-cell span{font-size:4.4px;line-height:1.8;color:#d8e8f6;display:block}
.gicon{width:12px;height:12px}

.area-list{font-size:4.6px;color:var(--text);line-height:11px;list-style:none}
.area-list li::before{content:"";display:inline-block;width:4px;height:4px;border-radius:50%;background:var(--blue);margin-right:4px}

.review{height:90px;background:#f3f4f6;padding:10px}
.avatar{width:10px;height:10px;border-radius:50%;background:#2f7a3b}
.stars{color:#f2b100;font-size:6px;letter-spacing:.5px}

.foot-h{font-family:"Montserrat",sans-serif;font-weight:600;font-size:6px;color:#fff}
.foot-list{list-style:none;font-size:4.6px;color:#c8d0d9;line-height:11px}
.foot-list li::before{content:"› "}
</style>
</head>
<body>

<!-- board header -->
<div class="abs brand-mark"><span class="brand-name"><span class="brand-dot"></span>KELVORN LLC</span></div>
<div class="abs vrule" style="left:495px"></div>
<div class="abs board-label" style="left:555px;top:90px">Fonts:</div>
<div class="abs font-name mont" style="left:555px;top:135px">Montserrat</div>
<div class="abs font-name" style="left:555px;top:160px;font-size:15px">Source Sans Pro</div>
<div class="abs vrule" style="left:712px"></div>
<div class="abs board-label" style="left:773px;top:90px">Colors:</div>
<div class="abs swatch" style="left:773px;background:var(--navy)"></div>
<div class="abs swatch" style="left:819px;background:var(--slate)"></div>
<div class="abs swatch" style="left:867px;background:var(--blue)"></div>
<div class="abs hex" style="left:766px">#3c4a59</div>
<div class="abs hex" style="left:812px">#6e7f92</div>
<div class="abs hex" style="left:860px">#0077c0</div>

<!-- desktop preview -->
<div class="screen" style="left:478px;top:276px;width:583px;height:331px">
  <div class="scaled" style="transform:scale(1.159)">
    <div class="hero">
      <div class="hero-photo" role="img" aria-label="Bright white kitchen interior with cabinets and marble floor"></div>
      <div class="abs call-label">CLICK TO CALL</div>
      <div class="abs call-pill"><span class="call-icon"></span>+1 234 567 890</div>
      <div class="abs call-hours">MON - SAT, 8 AM TO 6 PM</div>
      <div class="abs hero-logo"><span class="brand-name"><span class="brand-dot" style="width:6px;height:6px;margin-right:3px;vertical-align:1px"></span>KELVORN LLC</span></div>
      <div class="abs hero-menu">MENU ☰</div>
      <div class="abs banner banner--preview">WATER DAMAGE MITIGATION SPECIALISTS</div>
    </div>
  </div>
</div>

<!-- laptop preview -->
<div class="screen" style="left:169px;top:497px;width:381px;height:225px">
  <div class="scaled" style="transform:scale(.757)">
    <div class="hero">
      <div class="hero-photo" role="img" aria-label="Bright white kitchen interior with cabinets and marble floor"></div>
      <div class="abs call-label">CLICK TO CALL</div>
      <div class="abs call-pill"><span class="call-icon"></span>+1 234 567 890</div>
      <div class="abs call-hours">MON - SAT, 8 AM TO 6 PM</div>
      <div class="abs hero-logo"><span class="brand-name"><span class="brand-dot" style="width:6px;height:6px;margin-right:3px;vertical-align:1px"></span>KELVORN LLC</span></div>
      <div class="abs hero-menu">MENU ☰</div>
      <div class="abs banner banner--preview">WATER DAMAGE MITIGATION SPECIALISTS</div>
    </div>
  </div>
</div>

<!-- full page -->
<main class="page">
  <section class="hero">
    <div class="hero-photo" role="img" aria-label="Bright white kitchen interior with cabinets and marble floor"></div>
    <div class="abs call-label">CLICK TO CALL</div>
    <div class="abs call-pill"><span class="call-icon"></span>+1 234 567 890</div>
    <div class="abs call-hours">MON - SAT, 8 AM TO 6 PM</div>
    <div class="abs hero-logo"><span class="brand-name"><span class="brand-dot" style="width:6px;height:6px;margin-right:3px;vertical-align:1px"></span>KELVORN LLC</span></div>
    <div class="abs hero-menu">MENU ☰</div>
  </section>
  <div class="abs banner">WATER DAMAGE MITIGATION SPECIALISTS</div>

  <p class="abs small" style="left:68px;top:344px;width:150px">Lorem ipsum dolor sit amet, consectetur adipiscing elit, sed eiusmod tempor incididunt ut labore et dolore magna aliqua. Quis ipsum suspendisse ultrices gravida. Risus commodo viverra maecenas accumsan lacus vel facilisis.</p>
  <p class="abs small" style="left:287px;top:344px;width:150px">Lorem ipsum dolor sit amet, consectetur adipiscing elit, sed eiusmod tempor incididunt ut labore et dolore magna aliqua. Quis ipsum suspendisse ultrices gravida. Risus commodo viverra maecenas accumsan lacus vel facilisis.</p>
  <div class="abs rule" style="top:424px"></div>

  <!-- services -->
  <h2 class="abs sec-title" style="top:462px">- OUR SERVICES -</h2>
  <div class="abs tab" style="left:68px;top:499px;width:85px">WATER EXTRACTION</div>
  <div class="abs tab" style="left:162px;top:499px;width:85px">MITIGATION</div>
  <div class="abs tab" style="left:256px;top:499px;width:85px">RESTORATION</div>
  <div class="abs tab" style="left:351px;top:499px;width:85px">RECONSTRUCTION</div>
  <div class="abs svc-photo" style="left:68px;top:525px;width:85px;background:linear-gradient(160deg,#1d5fa8 0%,#3f8ad0 45%,#6a7480 70%,#2a5d94 100%)" role="img" aria-label="Water extraction hoses on wet floor"></div>
  <div class="abs svc-photo" style="left:162px;top:525px;width:85px;background:radial-gradient(circle at 50% 55%,#1f6fc0 0%,#2e7fce 35%,#8a959f 70%,#b8bfc6 100%)" role="img" aria-label="Blue air mover drying a room"></div>
  <div class="abs svc-photo" style="left:256px;top:525px;width:85px;background:linear-gradient(180deg,#c9cfd5 0%,#a8b1ba 40%,#3f78b8 70%,#7b858f 100%)" role="img" aria-label="Drying equipment set up in a hallway"></div>
  <div class="abs svc-photo" style="left:351px;top:525px;width:85px;background:linear-gradient(90deg,#eef1f4 0%,#d4dae0 45%,#2c6cac 70%,#9aa4ae 100%)" role="img" aria-label="Room under reconstruction with equipment"></div>
  <ul class="abs svc-list" style="left:68px;top:602px"><li>Lorem Ipsum Dolor Amet</li><li>Lorem Ipsum Dolor Amet</li><li>Lorem Ipsum Dolor Amet</li><li>Lorem Ipsum Dolor Amet</li><li>Lorem Ipsum Dolor Amet</li><li>Lorem Ipsum Dolor Amet</li></ul>
  <ul class="abs svc-list" style="left:162px;top:602px"><li>Lorem Ipsum Dolor Amet</li><li>Lorem Ipsum Dolor Amet</li><li>Lorem Ipsum Dolor Amet</li><li>Lorem Ipsum Dolor Amet</li><li>Lorem Ipsum Dolor Amet</li><li>Lorem Ipsum Dolor Amet</li></ul>
  <ul class="abs svc-list" style="left:256px;top:602px"><li>Lorem Ipsum Dolor Amet</li><li>Lorem Ipsum Dolor Amet</li><li>Lorem Ipsum Dolor Amet</li><li>Lorem Ipsum Dolor Amet</li><li>Lorem Ipsum Dolor Amet</li><li>Lorem Ipsum Dolor Amet</li></ul>
  <ul class="abs svc-list" style="left:351px;top:602px"><li>Lorem Ipsum Dolor Amet</li><li>Lorem Ipsum Dolor Amet</li><li>Lorem Ipsum Dolor Amet</li><li>Lorem Ipsum Dolor Amet</li><li>Lorem Ipsum Dolor Amet</li><li>Lorem Ipsum Dolor Amet</li></ul>
  <div class="abs btn" style="left:68px;top:674px;width:85px">EXPLORE SERVICE →</div>
  <div class="abs btn" style="left:162px;top:674px;width:85px">EXPLORE SERVICE →</div>
  <div class="abs btn" style="left:256px;top:674px;width:85px">EXPLORE SERVICE →</div>
  <div class="abs btn" style="left:351px;top:674px;width:85px">EXPLORE SERVICE →</div>

  <!-- pricing -->
  <section class="abs dark" style="top:736px;height:224px">
    <h2 class="abs sec-title" style="top:38px;color:#fff">- HOW WE PRICE -</h2>
    <div class="abs price-icon" style="left:68px;top:70px"></div>
    <div class="abs price-item" style="left:92px;top:70px"><b>FREE ESTIMATES</b><span>We can provide a free estimate so you know a price range before we show up.</span></div>
    <div class="abs price-icon" style="left:68px;top:113px;border-radius:50%"></div>
    <div class="abs price-item" style="left:92px;top:113px"><b>VOLUME BASED PRICING</b><span>Our pricing is based on the amount of the damage that has been caused.</span></div>
    <div class="abs price-icon" style="left:68px;top:157px"></div>
    <div class="abs price-item" style="left:92px;top:157px"><b>NO HIDDEN FEES</b><span>All water costs and other disposal fees are included in your upfront pricing.</span></div>
    <div class="abs" style="left:186px;top:124px;width:132px;text-align:center"><span class="brand-name" style="color:#fff;font-size:15px"><span class="brand-dot" style="background:#fff"></span>KELVORN LLC</span></div>
    <div class="abs price-item right" style="left:292px;top:70px"><b>MINIMUM LOADS</b><span>Lorem ipsum dolor sit amet, magna aliqua. Quis ipsum suspendisse ultrices.</span></div>
    <div class="abs price-icon" style="left:420px;top:70px"></div>
    <div class="abs price-item right" style="left:292px;top:113px"><b>UPFRONT PRICING</b><span>We always provide our customers with a firm price on site before we begin a job.</span></div>
    <div class="abs price-icon" style="left:420px;top:113px;border-radius:50%"></div>
    <div class="abs price-item right" style="left:292px;top:157px"><b>BETTER VALUE</b><span>Since we are not a national franchise with hefty franchise fees, we can pass along the savings.</span></div>
    <div class="abs price-icon" style="left:420px;top:157px"></div>
  </section>

  <!-- equipment -->
  <h2 class="abs mont" style="left:68px;top:1040px;font-size:11px;font-weight:600;line-height:1.35">- DECENT EQUIPMENTS,<br>DECENT RESULTS! -</h2>
  <p class="abs small" style="left:68px;top:1080px;width:150px">Lorem ipsum dolor sit amet, consectetur adipiscing elit, sed eiusmod tempor incididunt ut labore et dolore magna aliqua. Quis ipsum suspendisse ultrices gravida. Risus commodo viverra maecenas accumsan lacus vel facilisis.</p>
  <p class="abs small" style="left:68px;top:1128px;width:150px">Sed ut perspiciatis unde omnis iste natus error sit voluptatem accusantium doloremque laudantium, totam rem aperiam.</p>
  <div class="abs" style="left:237px;top:992px;width:202px;height:197px;border-radius:50%;background:linear-gradient(150deg,#ffffff 0%,#f2f4f6 30%,#5b6470 42%,#e9ecef 50%,#9fb4cc 62%,#3a5f8f 78%,#1f3f6a 100%)" role="img" aria-label="Technician in blue plaid shirt working on a ceiling duct"></div>

  <div class="abs rule" style="top:1230px"></div>
  <h2 class="abs sec-title" style="top:1268px">- OUR EQUIPMENT VS COMPETITORS -</h2>
  <div class="abs" style="left:68px;top:1310px;font-size:4.5px;color:var(--text)">OUR EQUIPMENT</div>
  <div class="abs bar-wrap" style="left:68px;top:1327px"><div class="bar" style="width:100%;background:var(--blue)"><span>Clean Complete Areas</span><span>95%</span></div></div>
  <div class="abs bar-wrap" style="left:68px;top:1347px"><div class="bar" style="width:100%;background:var(--slate)"><span>Dryness</span><span>98%</span></div></div>
  <div class="abs bar-wrap" style="left:68px;top:1367px"><div class="bar" style="width:100%;background:var(--navy)"><span>Clean Complete Areas</span><span>95%</span></div></div>
  <div class="abs" style="left:222px;top:1302px;width:54px;height:108px;border-radius:8px;background:linear-gradient(90deg,#0b5ea8 0%,#2f86d2 40%,#1f6fc0 70%,#0b4f90 100%)" role="img" aria-label="Blue commercial dehumidifier"></div>
  <div class="abs" style="left:312px;top:1310px;font-size:4.5px;color:var(--text)">COMPETITORS EQUIPMENT</div>
  <div class="abs bar-wrap" style="left:312px;top:1327px"><div class="bar" style="width:62%;background:var(--blue)"><span>Clean Complete Areas</span><span>60%</span></div></div>
  <div class="abs bar-wrap" style="left:312px;top:1347px"><div class="bar" style="width:62%;background:var(--slate)"><span>Dryness</span><span>55%</span></div></div>
  <div class="abs bar-wrap" style="left:312px;top:1367px"><div class="bar" style="width:62%;background:var(--navy)"><span>Clean Complete Areas</span><span>50%</span></div></div>

  <div class="abs rule" style="top:1454px"></div>
  <div class="abs" style="left:70px;top:1504px;width:165px;height:159px;border-radius:50%;background:#eceef1"></div>
  <div class="abs" style="left:44px;top:1526px;width:176px;height:112px;border-radius:22px 40px 14px 14px;background:linear-gradient(180deg,#4a5668 0%,#2f3a4a 55%,#1e2631 100%)" role="img" aria-label="Dark company service van"></div>
  <h2 class="abs mont" style="left:256px;top:1491px;font-size:10.5px;font-weight:600;line-height:1.35">3 SIMPLE WAYS TO GET YOUR<br>ESTIMATE TODAY!</h2>
  <div class="abs" style="left:256px;top:1533px;font-size:5px;color:var(--text)">Fast. Friendly. Professional. Reliable.</div>
  <div class="abs" style="left:256px;top:1560px;font-size:5px;color:var(--blue);font-weight:600">CALL US</div>
  <p class="abs small" style="left:256px;top:1567px;width:115px">Call us today and talk to one of our friendly, local staff members to discuss your needs.</p>
  <div class="abs pill-btn" style="left:381px;top:1565px;background:var(--blue)">CLICK TO CALL</div>
  <div class="abs" style="left:256px;top:1603px;font-size:5px;color:var(--blue);font-weight:600">TEXT US</div>
  <p class="abs small" style="left:256px;top:1610px;width:115px">Text us today with photos of the damage so we can provide you an estimate.</p>
  <div class="abs pill-btn" style="left:381px;top:1608px;background:var(--slate)">CLICK TO TEXT</div>
  <div class="abs" style="left:256px;top:1646px;font-size:5px;color:var(--blue);font-weight:600">EMAIL US</div>
  <p class="abs small" style="left:256px;top:1653px;width:115px">Email us by filling out our contact form and we will get back to you shortly.</p>
  <div class="abs pill-btn" style="left:381px;top:1651px;background:var(--navy)">CLICK TO MAIL</div>

  <!-- why us -->
  <section class="abs blue-band" style="top:1713px;height:354px">
    <h2 class="abs sec-title" style="top:37px;color:#fff">- WHY CHOOSING KELVORN? -</h2>
    <div class="abs grid-cell" style="left:68px;top:73px"><svg class="gicon" viewBox="0 0 12 12"><rect x="1" y="2" width="10" height="9" fill="none" stroke="#fff"/><path d="M1 5h10" stroke="#fff"/></svg><b>EASY SCHEDULING</b><span>Just give us a call, text or contact us by email for same day or next day service when available.</span></div>
    <div class="abs grid-cell" style="left:191px;top:73px"><svg class="gicon" viewBox="0 0 12 12"><path d="M1 7l3-3 3 2 4-4" fill="none" stroke="#fff"/></svg><b>UPFRONT PRICING</b><span>When we get there we let you know everything you need and you will be sure of a price with no hidden fees.</span></div>
    <div class="abs grid-cell" style="left:314px;top:73px"><svg class="gicon" viewBox="0 0 12 12"><circle cx="6" cy="4" r="2.5" fill="none" stroke="#fff"/><path d="M2 11c0-3 8-3 8 0" fill="none" stroke="#fff"/></svg><b>PROFESSIONAL SERVICES</b><span>Our uniformed team members are friendly, professional, background checked and diligent workers.</span></div>
    <div class="abs grid-cell" style="left:68px;top:192px"><svg class="gicon" viewBox="0 0 12 12"><rect x="2" y="2" width="8" height="9" fill="none" stroke="#fff"/></svg><b>ALL CLEANED UP</b><span>When we're all done and ready to go, we will check with you to make sure we removed everything you wanted.</span></div>
    <div class="abs grid-cell" style="left:191px;top:192px"><svg class="gicon" viewBox="0 0 12 12"><ellipse cx="6" cy="5" rx="5" ry="3.5" fill="none" stroke="#fff"/></svg><b>EXCELLENT COMMUNICATION</b><span>We will always keep you in the loop. We'll confirm your appointment with a 1 hour block of time.</span></div>
    <div class="abs grid-cell" style="left:314px;top:192px"><svg class="gicon" viewBox="0 0 12 12"><rect x="1" y="3" width="10" height="7" rx="1" fill="none" stroke="#fff"/><path d="M1 5h10" stroke="#fff"/></svg><b>EASY PAYMENT METHODS</b><span>When we have completed your service we are ready for payment; we accept cash, checks and credit cards.</span></div>
  </section>

  <!-- areas -->
  <h2 class="abs mont" style="left:68px;top:2137px;font-size:11px;font-weight:600">- WORKING AREAS -</h2>
  <p class="abs small" style="left:68px;top:2156px;width:160px">Kelvorn LLC offers our water extractions, mitigation, demo, restoration, and reconstruction services in most of the Texas. Contact us if your area is not listed below to see if we can help.</p>
  <ul class="abs area-list" style="left:68px;top:2206px"><li>Northside</li><li>Oakridge</li><li>Fairmount</li><li>Eastgate</li></ul>
  <ul class="abs area-list" style="left:124px;top:2206px"><li>Lake Heights</li><li>Westfield</li><li>Elm Bay</li><li>Cedar Point</li></ul>
  <div class="abs" style="left:273px;top:2111px;width:166px;height:166px;border-radius:50%;background:linear-gradient(135deg,#f6f7f9 0%,#e9edf1 35%,#f3f5f7 50%,#dfe5ec 70%,#eef1f4 100%)" role="img" aria-label="Street map of the service area"></div>
  <div class="abs" style="left:273px;top:2223px;width:34px;height:34px;border-radius:50%;background:var(--navy)">
    <svg width="34" height="34" viewBox="0 0 34 34"><path d="M17 10a5 5 0 0 0-5 5c0 4 5 9 5 9s5-5 5-9a5 5 0 0 0-5-5z" fill="#fff"/><circle cx="17" cy="15" r="2" fill="#3c4a59"/></svg>
  </div>

  <div class="abs" style="left:68px;top:2313px;width:368px;height:62px;background:var(--blue);color:#fff">
    <div class="abs mont" style="left:22px;top:20px;font-size:9px;letter-spacing:.4px">WE OFFER SAME &amp; NEXT DAY SERVICE.</div>
    <div class="abs mont" style="left:22px;top:32px;font-size:9px;font-weight:700">SCHEDULE YOUR APPOINTMENT NOW!</div>
    <div class="abs pill-btn" style="left:290px;top:22px;width:52px;background:#fff;color:var(--blue)">CONTACT US</div>
  </div>

  <!-- reviews -->
  <h2 class="abs sec-title" style="top:2414px">- CLIENT REVIEWS -</h2>
  <div class="abs" style="left:60px;top:2488px;font-size:6px;color:#b7bec6">‹</div>
  <div class="abs" style="left:440px;top:2488px;font-size:6px;color:#b7bec6">›</div>
  <div class="abs review" style="left:68px;top:2447px;width:114px"><span class="abs avatar" style="left:10px;top:10px"></span><div style="margin-left:16px;font-size:4.6px;font-weight:600">Dana Whitlock</div><div style="margin-left:16px;font-size:4px;color:#aab">2 weeks ago</div><div class="stars" style="margin-left:16px">★★★★★</div><p class="small" style="font-size:4.6px;margin-top:3px">Lorem ipsum dolor sit amet, at duis tell mode consectetur adipiscing elit, sed do mod tempor incididunt ut labore et dolore magna aliqua sit.</p></div>
  <div class="abs review" style="left:193px;top:2447px;width:115px"><span class="abs avatar" style="left:10px;top:10px"></span><div style="margin-left:16px;font-size:4.6px;font-weight:600">Dana Whitlock</div><div style="margin-left:16px;font-size:4px;color:#aab">2 weeks ago</div><div class="stars" style="margin-left:16px">★★★★★</div><p class="small" style="font-size:4.6px;margin-top:3px">Lorem ipsum dolor sit amet, at duis tell mode consectetur adipiscing elit, sed do mod tempor incididunt ut labore et dolore magna aliqua sit.</p></div>
  <div class="abs review" style="left:318px;top:2447px;width:118px"><span class="abs avatar" style="left:10px;top:10px"></span><div style="margin-left:16px;font-size:4.6px;font-weight:600">Dana Whitlock</div><div style="margin-left:16px;font-size:4px;color:#aab">2 weeks ago</div><div class="stars" style="margin-left:16px">★★★★★</div><p class="small" style="font-size:4.6px;margin-top:3px">Lorem ipsum dolor sit amet, at duis tell mode consectetur adipiscing elit, sed do mod tempor incididunt ut labore et dolore magna aliqua sit.</p></div>
  <div class="abs" style="left:0;top:2555px;width:503px;text-align:center;font-size:4.6px;color:var(--text)">Client rating score 4.9 of 5, based on 73 reviews</div>
  <div class="abs" style="left:0;top:2567px;width:503px;text-align:center;font-size:4.6px;color:var(--navy);text-decoration:underline">CLICK HERE TO READ MORE REVIEWS</div>

  <!-- footer -->
  <footer class="abs dark" style="top:2613px;height:188px">
    <div class="abs" style="left:68px;top:68px"><span class="brand-name" style="color:#fff;font-size:14px"><span class="brand-dot" style="background:#fff"></span>KELVORN LLC</span></div>
    <div class="abs foot-h" style="left:195px;top:38px">LINKS</div>
    <ul class="abs foot-list" style="left:195px;top:52px"><li>Home</li><li>Services</li><li>How We Price</li><li>Areas</li><li>Reviews</li><li>Contact</li></ul>
    <div class="abs foot-h" style="left:275px;top:38px">SERVICES</div>
    <ul class="abs foot-list" style="left:275px;top:52px"><li>Water Extraction</li><li>Mitigation</li><li>Demo</li><li>Restoration</li><li>Reconstruction</li></ul>
    <div class="abs foot-h" style="left:362px;top:38px">CONTACT US</div>
    <div class="abs" style="left:362px;top:55px;width:14px;height:14px;border-radius:50%;border:1px solid #9aa6b3"></div>
    <div class="abs" style="left:382px;top:55px;font-size:4.6px;color:#fff;font-weight:600">Call Us At<br><span style="font-weight:400;color:#c8d0d9">1 234 567 890</span></div>
    <div class="abs" style="left:362px;top:90px;width:14px;height:14px;border-radius:50%;border:1px solid #9aa6b3"></div>
    <div class="abs" style="left:382px;top:90px;font-size:4.6px;color:#fff;font-weight:600">Working Hours<br><span style="font-weight:400;color:#c8d0d9">Mon to Sat - 8 AM to 6 PM</span></div>
    <div class="abs" style="left:0;top:156px;width:503px;text-align:center;font-size:4.4px;color:#c8d0d9">Copyright 2024 KELVORN - All Rights Reserved</div>
  </footer>
</main>

</body>
</html>
```